Looking for a creative label design for our retail coffee bags

We are a coffee manufacturer (coffee roaster) looking to re-brand our retail label for our coffee bags. Our main coffee blend that we sell is our Harborline Velvet Blend. You can use this name when creating the label. We are going for a look that represents our company as a coffee roaster. Please reference our website (www.brindlemugworks.com) and our Facebook page to learn more about our company and to give you more inspiration on creating this design.

Target Market(s)

Retail customers/grocery stores

Industry/Entity Type

Manufacturer

Requirements
Must have
• The size of the label has to be 3" width x 4" height

Logo must be Black
Nice to have
• We currently incorporate a color on our labels for each blend. For example, Harborline Velvet Blend (royal blue), Decaffeinated Blend (red), Breakfast Blend (green), Flavored coffees (gold).

Rustic/vintage style

```html
<!DOCTYPE html>
<html lang="en">
<head>
<meta charset="utf-8">
<title>Brindle Mugworks – Harborline Velvet Blend label</title>
<link href="https://fonts.googleapis.com/css2?family=Archivo:wght@400;500;800&display=swap" rel="stylesheet">
<style>
  :root {
    --blush: #fce6e7;
    --blush-deep: #eed3d5;
    --ink: #0a0a0a;
    --ink-soft: #262626;
    --paper: #ffffff;
    --royal-blue: #506ba8;
  }
  html, body {
    margin: 0;
    padding: 0;
    width: 1200px;
    height: 792px;
    overflow: hidden;
    background: var(--ink);
  }
  .label-sheet {
    display: block;
    width: 1200px;
    height: 792px;
    font-family: "Archivo", "Helvetica Neue", Arial, sans-serif;
  }
  .bg-light { fill: var(--blush); }
  .bg-dark { fill: var(--ink); }
  .bean-field-light { fill: var(--blush-deep); }
  .bean-field-dark { fill: var(--ink-soft); }
  .blend-band { fill: var(--royal-blue); }
  .seal-halo-light { fill: var(--blush); }
  .seal-halo-dark { fill: var(--ink); }
  .seal-core-light { fill: var(--ink); }
  .seal-core-dark { fill: var(--paper); }
  .seal-ring-light { fill: none; stroke: var(--blush); stroke-width: 0.6; }
  .seal-ring-dark { fill: none; stroke: var(--ink); stroke-width: 0.6; }
  .brand-name { font-weight: 500; font-size: 25px; letter-spacing: 1px; text-anchor: middle; }
  .brand-light { fill: var(--blush); }
  .brand-dark { fill: var(--ink); }
  .tagline { font-weight: 500; font-size: 5px; letter-spacing: 1.4px; text-transform: uppercase; }
  .tagline-light { fill: var(--ink); }
  .tagline-dark { fill: var(--paper); }
  .blend-origin { font-weight: 800; font-size: 31px; fill: var(--paper); text-anchor: end; letter-spacing: 0.5px; }
  .blend-name { font-weight: 800; font-size: 22px; fill: var(--ink); text-anchor: end; }
  .blend-note { font-weight: 400; font-size: 13px; fill: var(--paper); text-anchor: end; }
  .net-weight { font-weight: 400; font-size: 13px; text-anchor: end; }
  .net-light { fill: var(--ink); }
  .net-dark { fill: var(--paper); }
</style>
</head>
<body>
<svg class="label-sheet" viewBox="0 0 1200 792" xmlns="http://www.w3.org/2000/svg">
  <defs>
    <path id="tagline-arc-light" d="M215 242 A107 107 0 0 0 391 242"/>
    <path id="tagline-arc-dark" d="M817 242 A107 107 0 0 0 993 242"/>
  </defs>

  <!-- Light label -->
  <g class="label label-light">
    <rect class="bg-light" x="0" y="0" width="598" height="792"/>
    <rect class="bean-field-light" x="95" y="59" width="173" height="590" rx="40" role="img" aria-label="Hand-drawn coffee bean illustrations scattered down the left side"/>
    <path class="blend-band" d="M270 59 H508 V620 Q411 697 270 689 Z"/>
    <circle class="seal-halo-light" cx="310" cy="183" r="110"/>
    <circle class="seal-core-light" cx="303" cy="180" r="103"/>
    <circle class="seal-ring-light" cx="303" cy="180" r="94"/>
    <text class="brand-name brand-light" x="303" y="175">BRINDLE</text>
    <text class="brand-name brand-light" x="303" y="204">MUGWORKS</text>
    <text class="tagline tagline-light"><textPath href="#tagline-arc-light">Proudly roasted in Alder Falls since 1994.</textPath></text>
    <text class="blend-origin" x="488" y="519">HARBORLINE</text>
    <text class="blend-name" x="488" y="550">VELVET BLEND</text>
    <text class="blend-note" x="488" y="572">FRESH ROASTED</text>
    <text class="net-weight net-light" x="488" y="754">NET WT. 10 OZ (284g)</text>
  </g>

  <!-- Dark label -->
  <g class="label label-dark">
    <rect class="bg-dark" x="598" y="0" width="602" height="792"/>
    <rect class="bean-field-dark" x="697" y="59" width="173" height="590" rx="40" role="img" aria-label="Hand-drawn coffee bean illustrations scattered down the left side"/>
    <path class="blend-band" d="M872 59 H1109 V620 Q1012 697 872 689 Z"/>
    <circle class="seal-halo-dark" cx="912" cy="183" r="110"/>
    <circle class="seal-core-dark" cx="905" cy="180" r="103"/>
    <circle class="seal-ring-dark" cx="905" cy="180" r="94"/>
    <text class="brand-name brand-dark" x="905" y="175">BRINDLE</text>
    <text class="brand-name brand-dark" x="905" y="204">MUGWORKS</text>
    <text class="tagline tagline-dark"><textPath href="#tagline-arc-dark">Proudly roasted in Alder Falls since 1994.</textPath></text>
    <text class="blend-origin" x="1089" y="519">HARBORLINE</text>
    <text class="blend-name" x="1089" y="550">VELVET BLEND</text>
    <text class="blend-note" x="1089" y="572">FRESH ROASTED</text>
    <text class="net-weight net-dark" x="1089" y="754">NET WT. 10 OZ (284g)</text>
  </g>
</svg>
</body>
</html>
```